Optometrist/Eye Care Clinic Business card with new logo attached

We are a small, independent eye care clinic in Canada. We have recently updated our logo (as attached), and would like a professional, modern and health care oriented business card to highlight our office details and our optometrist. We'd like to incorporate the blue colours as seen on our logo.

Target Market(s)

demographic: age 35-65 male/female equal

Industry/Entity Type

Health Care

Contact Information for Business Card

Name of clinic: "Marrow Bend Eye Care Optometry"

Font styles to use
Sans Serif

Colors
0355a3

Requirements
Must have
• our website: marrowbendeyecare.com
• Dr Lena Quorvik
• Optometrist
• 217-392 E Halvering Ave
• Vancouver BC V6R 3J8
• P: 604-319-2058
• E: info@marrowbendeyecare.com
Nice to have
• front side: logo/name of clinic as seen on logo attached and website
• backside: logo on the left side, and name/title/address/phone/email

```html
<!DOCTYPE html>
<html lang="en">
<head>
<meta charset="utf-8">
<title>Marrow Bend Eye Care Optometry – Business Card</title>
<link href="https://fonts.googleapis.com/css2?family=Open+Sans:wght@400;600&display=swap" rel="stylesheet">
<style>
  :root {
    --brand-blue: #0355a3;
    --brand-navy: #0b2f5c;
    --brand-mid: #2f6fa8;
    --card-white: #ffffff;
    --backdrop: #e9ebee;
    --rule: #1d3f6e;
  }
  * { box-sizing: border-box; margin: 0; padding: 0; }
  html, body {
    width: 1200px; height: 1195px; overflow: hidden;
    background: var(--backdrop);
  }
  .sheet {
    width: 1200px; height: 1195px;
    display: flex; flex-direction: column;
    align-items: center; justify-content: center; gap: 70px;
  }
  .card {
    width: 700px; height: 400px; position: relative;
    box-shadow: 0 6px 22px rgba(0,0,0,.16);
    overflow: hidden;
    font-family: "Open Sans", sans-serif;
  }

  /* Front */
  .card--front { background: var(--brand-blue); }
  .front-name {
    position: absolute; left: 0; right: 0; top: 150px;
    text-align: center;
    font-weight: 400; font-size: 28px; line-height: 1.2;
    color: var(--card-white);
  }
  .front-band {
    position: absolute; left: 0; right: 0; bottom: 62px; height: 44px;
    background: var(--card-white);
    display: flex; align-items: center; justify-content: center;
    font-weight: 600; font-size: 16px; letter-spacing: 7px; text-transform: uppercase;
    color: var(--brand-blue);
  }

  /* Back */
  .card--back { background: var(--card-white); }
  .back-name {
    position: absolute; left: 46px; top: 0; bottom: 0; width: 290px;
    display: flex; align-items: center;
    font-weight: 400; font-size: 22px; line-height: 1.3;
    color: var(--brand-blue);
  }
  .back-rule {
    position: absolute; left: 362px; top: 90px; bottom: 90px;
    width: 2px; background: var(--rule);
  }
  .back-details {
    position: absolute; left: 392px; top: 112px;
    color: var(--brand-mid);
    font-size: 14px; line-height: 1.55;
  }
  .doctor { font-size: 20px; font-weight: 600; color: var(--brand-navy); line-height: 1.2; }
  .role { font-size: 13px; color: var(--brand-mid); margin-bottom: 14px; }
  .address { margin-bottom: 10px; }
  .contact-row { display: flex; align-items: center; gap: 8px; }
  .contact-row svg { width: 14px; height: 14px; flex: none; }
</style>
</head>
<body>
<main class="sheet">

  <section class="card card--front" aria-label="Business card front">
    <p class="front-name">Marrow Bend Eye Care<br>Optometry</p>
    <div class="front-band">marrowbendeyecare.com</div>
  </section>

  <section class="card card--back" aria-label="Business card back">
    <p class="back-name">Marrow Bend Eye Care<br>Optometry</p>
    <div class="back-rule" aria-hidden="true"></div>
    <div class="back-details">
      <p class="doctor">Dr Lena Quorvik</p>
      <p class="role">Optometrist</p>
      <p class="address">217-392 E Halvering Ave<br>Vancouver BC V6R 3J8</p>
      <p class="contact-row">
        <svg viewBox="0 0 24 24" aria-hidden="true"><path fill="#0b2f5c" d="M6.6 10.8a15 15 0 0 0 6.6 6.6l2.2-2.2c.3-.3.7-.4 1-.2 1.1.4 2.3.6 3.6.6.6 0 1 .4 1 1V20c0 .6-.4 1-1 1A17 17 0 0 1 3 4c0-.6.4-1 1-1h3.5c.6 0 1 .4 1 1 0 1.3.2 2.5.6 3.6.1.3 0 .7-.2 1z"/></svg>
        604-319-2058
      </p>
      <p class="contact-row">
        <svg viewBox="0 0 24 24" aria-hidden="true"><rect x="3" y="5" width="18" height="14" rx="1.5" fill="none" stroke="#0b2f5c" stroke-width="2"/><path d="M3.5 6l8.5 7 8.5-7" fill="none" stroke="#0b2f5c" stroke-width="2"/></svg>
        info@marrowbendeyecare.com
      </p>
    </div>
  </section>

</main>
</body>
</html>
```